A5 Flyer for Financial Services Business

I am after a re-design of our business flyer to fit in with our new branding style and logo colour scheme. Wanting something with a bit of designer flair that I could not create myself. I have included the flyer which I created which lacks style so dazzle me.

I want to use the same content.

Text for main body of flyer is

Are you a small business owner, tradie or KTAV Service Provider struggling to stay on top of your bookkeeping and compliance obligations? If so we would love to help you get back on track and take control of your business finances so that you can make informed business decisions and focus on what you do best.

We have over 20 years industry experience and, as a small business ourselves, we are able to offer our clients a personal bookkeeping solution tailored to meet the needs of your business.

Accounts Payable | Accounts Receivable
Customer Invoicing
Bank and Credit Card Reconciliations
Payroll | Superannuation | Payroll Tax
Business Activity | Instalment Activity Statements
Regular Financial Reports
Ledgra and TallyBooks Set-Up and Training

```html
<!DOCTYPE html>
<html lang="en">
<head>
<meta charset="utf-8">
<title>Even Keel Financial Services – Bookkeeping Flyer</title>
<link href="https://fonts.googleapis.com/css2?family=Hind:wght@400;500;600;700&display=swap" rel="stylesheet">
<style>
  :root{
    --teal:#0f9f9a;
    --teal-mid:#0b7a85;
    --navy:#05324a;
    --ink:#0d1a22;
    --paper:#f4f5f6;
    --mist:#e2e6ea;
  }
  *{margin:0;padding:0;box-sizing:border-box}
  html,body{width:808px;height:1200px;overflow:hidden;background:#fff}
  body{font-family:"Hind",sans-serif;color:var(--ink)}
  .flyer{position:relative;width:808px;height:1200px;background:linear-gradient(180deg,#fff 0%,var(--paper) 30%,#fafafa 70%,#fff 100%);overflow:hidden}

  .hero-photo{position:absolute;left:3px;top:62px;width:805px;height:285px;
    background:linear-gradient(115deg,#eceef1 0%,#e6dcd6 35%,#d9dde3 60%,#9fb1bf 85%,#7d8f9e 100%)}
  .hero-wave{position:absolute;left:0;top:62px;width:808px;height:285px}

  .brand{position:absolute;left:57px;top:178px;color:var(--teal-mid);font-weight:600;line-height:1}
  .brand-mark{display:inline-block;width:22px;height:22px;background:var(--teal-mid);vertical-align:middle;margin-right:8px}
  .brand-name{font-size:28px;vertical-align:middle;letter-spacing:-.3px}
  .brand-sub{display:block;font-size:14px;letter-spacing:6px;margin-top:6px;margin-left:30px}

  .headline{position:absolute;left:50px;top:366px;font-size:43px;font-weight:700;line-height:44px;letter-spacing:-.4px;
    background:linear-gradient(90deg,var(--teal) 0%,var(--teal-mid) 45%,var(--navy) 80%);
    -webkit-background-clip:text;background-clip:text;color:transparent}

  .intro{position:absolute;left:52px;top:473px;width:633px;height:139px;border-left:4px solid var(--teal-mid);
    padding-left:11px;font-size:21px;line-height:27px;font-weight:500}
  .intro-accent{position:absolute;left:703px;top:473px;width:52px;height:139px;background:var(--teal-mid)}

  .desk-frame{position:absolute;left:84px;top:637px;width:189px;height:134px;background:var(--navy);border-top:4px solid var(--teal)}
  .desk-photo{position:absolute;left:66px;top:643px;width:202px;height:128px;border-radius:18px 18px 18px 18px;
    background:linear-gradient(135deg,#3a3f46 0%,#c9a27a 45%,#e8d7c3 70%,#2b2f35 100%)}

  .experience{position:absolute;left:290px;top:628px;width:470px;font-size:19px;line-height:23px;font-weight:500}
  .experience-lead{font-size:22px;font-weight:600}
  .experience-row{display:flex;align-items:flex-start;margin-top:-4px}
  .experience-num{font-size:66px;font-weight:600;line-height:62px;color:var(--teal-mid);
    background:linear-gradient(90deg,var(--teal),var(--navy));-webkit-background-clip:text;background-clip:text;color:transparent;margin-right:10px}
  .experience-years{font-size:22px;font-weight:600;line-height:22px}
  .experience-first{display:block;margin-top:8px}

  .bird{position:absolute;left:500px;top:730px;width:295px;height:340px;border-radius:50%;
    background:radial-gradient(ellipse at 55% 50%,rgba(235,237,240,.85) 0%,rgba(220,224,228,.45) 45%,rgba(255,255,255,0) 72%);z-index:3}

  .services{position:absolute;left:52px;top:801px;width:703px;height:220px;
    background:linear-gradient(100deg,#0a2238 0%,var(--navy) 35%,var(--teal-mid) 70%,var(--teal) 100%);
    padding:12px 0 0 15px;color:#fff;font-size:22px;line-height:28.8px;list-style:none;z-index:2}
  .services .sep{display:inline-block;width:3px;height:22px;background:#fff;margin:0 5px;vertical-align:-1px}

  .accreditations{position:absolute;left:68px;top:1028px;display:flex;gap:46px;font-size:21px;font-weight:500;list-style:none}
  .accreditations li{display:flex;align-items:center}
  .accreditations li::before{content:"";width:10px;height:10px;border-radius:50%;background:var(--teal-mid);margin-right:12px}

  .phone{position:absolute;left:68px;top:1075px;font-size:46px;font-weight:700;color:var(--navy);letter-spacing:.5px}
  .phone-rule{position:absolute;left:373px;top:1110px;width:291px;height:4px;background:linear-gradient(90deg,var(--teal),var(--navy))}
  .website{position:absolute;left:70px;top:1120px;font-size:28px;font-weight:500;color:var(--ink);letter-spacing:.4px}
</style>
</head>
<body>
<main class="flyer">
  <div class="hero-photo" role="img" aria-label="Close-up of a hand using a calculator with pen, glasses and notebook, overlaid with a rising line chart"></div>
  <svg class="hero-wave" viewBox="0 0 808 285" aria-hidden="true">
    <defs>
      <linearGradient id="waveFill" x1="0" x2="1" y1="0" y2="0">
        <stop offset="0" stop-color="#0f9f9a"/>
        <stop offset=".55" stop-color="#0b7a85"/>
        <stop offset="1" stop-color="#05324a"/>
      </linearGradient>
    </defs>
    <path d="M0 170 C60 215 110 250 200 245 C330 238 430 165 560 110 C660 70 740 40 808 40 L808 88 C740 86 660 100 570 130 C440 175 330 250 200 252 C110 254 50 215 0 180 Z" fill="url(#waveFill)"/>
  </svg>

  <div class="brand">
    <span class="brand-mark"></span><span class="brand-name">EVEN KEEL</span>
    <span class="brand-sub">Financial Services</span>
  </div>

  <h1 class="headline">Bookkeeping Tailored<br>to your Business Needs</h1>

  <p class="intro">Are you a small business owner, tradie or KTAV Service Provider struggling to stay on top of your bookkeeping and compliance obligations? If so we would love to help you get back on track and take control of your business finances so that you can make informed business decisions and focus on what you do best.</p>
  <div class="intro-accent"></div>

  <div class="desk-frame"></div>
  <div class="desk-photo" role="img" aria-label="Hands using a calculator beside a laptop and printed charts on a desk"></div>

  <div class="experience">
    <div class="experience-lead">We have over</div>
    <div class="experience-row">
      <span class="experience-num">20</span>
      <span class="experience-years">years<span class="experience-first" style="font-size:19px;font-weight:500">industry experience and, as a small business</span></span>
    </div>
    <div>ourselves, we are able to offer our clients a personal bookkeeping solution tailored to meet the needs of your business.</div>
  </div>

  <ul class="services">
    <li>Accounts Payable<span class="sep"></span>Accounts Receivable</li>
    <li>Customer Invoicing</li>
    <li>Bank and Credit Card Reconciliations</li>
    <li>Payroll<span class="sep"></span>Superannuation<span class="sep"></span>Payroll Tax</li>
    <li>Business Activity<span class="sep"></span>Instalment Activity Statements</li>
    <li>Regular Financial Reports</li>
    <li>Ledgra and TallyBooks Set-Up and Training</li>
  </ul>

  <div class="bird" role="img" aria-label="Large pale silver hummingbird in flight"></div>

  <ul class="accreditations">
    <li>Ledgra Certified Advisor</li>
    <li>TallyBooks Pro Advisor</li>
  </ul>

  <div class="phone">0400 372 918</div>
  <div class="phone-rule"></div>
  <div class="website">www.evenkeelfinancialservices.com.au</div>
</main>
</body>
</html>
```